Postcard Design Project

We sells Laser Printer Ink and Toners, We also sells on Zephra Market Place, Need a post card for these zephra contact to start buying through our website instead of Zephra. Company Name: Kv Business Supplies LLC, website is www.kvtoner.example phone#555-203-4471

```html
<!DOCTYPE html>
<html lang="en">
<head>
<meta charset="utf-8">
<title>Kv Business Supplies – Postcard</title>
<link href="https://fonts.googleapis.com/css2?family=Montserrat:wght@700;800&family=Arimo:wght@400;700&display=swap" rel="stylesheet">
<style>
  :root {
    --ink-black: #121212;
    --brand-yellow: #f7d000;
    --brand-magenta: #e8168c;
    --brand-cyan: #29abe2;
    --paper-white: #ffffff;
    --stage-grey: #ececec;
    --photo-dark: #2e231d;
    --photo-light: #d9d9d9;
  }
  * { margin: 0; padding: 0; box-sizing: border-box; }
  html, body { width: 1200px; height: 1155px; overflow: hidden; background: var(--stage-grey); }
  .stage { position: relative; width: 1200px; height: 1155px; }
  .postcard {
    position: absolute; top: 375px; width: 560px; height: 405px;
    box-shadow: 3px 4px 8px rgba(0,0,0,.35); overflow: hidden;
  }
  .postcard--front { left: 20px; background: var(--ink-black); }
  .postcard--back { left: 620px; background: var(--paper-white); }
  .postcard svg.art { position: absolute; inset: 0; }
  .layer { position: absolute; }

  .header-line {
    left: 0; top: 0; width: 100%; height: 47px; line-height: 47px; text-align: center;
    font-family: "Montserrat", sans-serif; font-weight: 800; font-size: 19px; color: var(--brand-yellow);
  }
  .headline {
    left: 34px; top: 112px; font-family: "Montserrat", sans-serif; font-weight: 800;
    font-size: 50px; line-height: 49px; color: var(--paper-white);
  }
  .headline .accent { color: var(--brand-yellow); display: block; }
  .brand-name {
    font-family: "Montserrat", sans-serif; font-weight: 800; color: var(--ink-black); white-space: nowrap;
    display: flex; align-items: center; gap: 7px;
  }
  .brand-name .dot { width: 16px; height: 16px; border-radius: 50%; background: var(--brand-magenta); }
  .front-brand { left: 318px; top: 232px; font-size: 15px; }
  .offer {
    left: 34px; top: 303px; font-family: "Arimo", sans-serif; font-size: 20px; line-height: 23px;
    color: var(--paper-white); text-transform: uppercase;
  }
  .contact-bar {
    left: 34px; top: 360px; height: 45px; line-height: 45px; font-family: "Montserrat", sans-serif;
    font-weight: 700; font-size: 20px; letter-spacing: 3px; color: var(--paper-white); white-space: nowrap;
  }
  .contact-bar .web { color: var(--brand-yellow); }

  .back-header { width: 281px; font-size: 19px; }
  .back-contact {
    left: 0; top: 296px; width: 281px; text-align: center; font-family: "Montserrat", sans-serif;
    font-weight: 700; color: var(--ink-black);
  }
  .back-contact .brand-name { justify-content: center; font-size: 14px; margin-bottom: 10px; }
  .back-contact .phone, .back-contact .web { font-size: 19px; line-height: 22px; }
</style>
</head>
<body>
<main class="stage">

  <section class="postcard postcard--front">
    <svg class="art" viewBox="0 0 560 405" width="560" height="405">
      <defs>
        <linearGradient id="darkPhoto" x1="0" y1="0" x2="1" y2="1">
          <stop offset="0" stop-color="#4a3a2f"/><stop offset="1" stop-color="#1c1613"/>
        </linearGradient>
        <linearGradient id="printerPhoto" x1="0" y1="0" x2="0" y2="1">
          <stop offset="0" stop-color="#5a5a5e"/><stop offset="1" stop-color="#c8c8c8"/>
        </linearGradient>
      </defs>
      <rect x="0" y="0" width="560" height="405" fill="var(--ink-black)"/>
      <polygon points="0,49 180,49 174,57 0,57" fill="var(--brand-yellow)"/>
      <polygon points="180,49 230,49 224,57 174,57" fill="var(--brand-cyan)"/>
      <polygon points="230,47 560,47 560,62 222,62" fill="var(--brand-magenta)"/>
      <rect x="0" y="62" width="560" height="223" fill="var(--paper-white)"/>
      <polygon role="img" aria-label="Close-up photo of a printer control panel" points="0,62 235,62 326,285 0,285" fill="url(#darkPhoto)"/>
      <polygon role="img" aria-label="Photo of two wide-format printers" points="270,70 548,70 548,225 335,225" fill="url(#printerPhoto)"/>
      <polygon points="0,66 8,66 40,120 32,120" fill="var(--paper-white)"/>
      <polygon points="14,66 22,66 54,120 46,120" fill="var(--brand-cyan)"/>
      <polygon points="28,66 36,66 68,120 60,120" fill="var(--brand-magenta)"/>
      <polygon points="46,66 55,66 87,120 78,120" fill="var(--brand-yellow)"/>
      <polygon points="0,283 380,283 372,295 0,295" fill="var(--brand-yellow)"/>
      <polygon points="0,295 488,295 468,360 0,360" fill="var(--brand-cyan)"/>
      <polygon points="470,300 560,300 560,360 500,360" fill="var(--brand-magenta)"/>
      <g stroke="var(--ink-black)" stroke-width="3">
        <line x1="455" y1="290" x2="505" y2="360"/><line x1="463" y1="290" x2="513" y2="360"/>
        <line x1="471" y1="290" x2="521" y2="360"/><line x1="479" y1="290" x2="529" y2="360"/>
        <line x1="487" y1="290" x2="537" y2="360"/><line x1="495" y1="290" x2="545" y2="360"/>
      </g>
      <polygon points="515,255 523,255 560,315 560,328" fill="var(--brand-cyan)"/>
      <polygon points="528,255 536,255 560,294 560,307" fill="var(--brand-magenta)"/>
      <polygon points="541,255 549,255 560,273 560,286" fill="var(--brand-yellow)"/>
      <rect x="0" y="360" width="560" height="45" fill="var(--ink-black)"/>
    </svg>
    <p class="layer header-line">GET A TECHNICIAN IN YOUR OFFICE TODAY!</p>
    <h1 class="layer headline">GOT<span class="accent">DIRTY</span>PRINTER?</h1>
    <div class="layer brand-name front-brand"><span class="dot"></span>Kv Business Supplies</div>
    <p class="layer offer">Also check out our unbeatable<br>ink and toner online prices</p>
    <p class="layer contact-bar">555-203-4471 | <span class="web">www.kvtoner.example</span></p>
  </section>

  <section class="postcard postcard--back">
    <svg class="art" viewBox="0 0 560 405" width="560" height="405">
      <defs>
        <linearGradient id="repairPhoto" x1="0" y1="0" x2="1" y2="1">
          <stop offset="0" stop-color="#6e7a5c"/><stop offset=".5" stop-color="#cfc9b8"/><stop offset="1" stop-color="#2a3140"/>
        </linearGradient>
      </defs>
      <rect x="0" y="0" width="281" height="47" fill="var(--ink-black)"/>
      <polygon points="0,47 165,47 159,55 0,55" fill="var(--brand-magenta)"/>
      <polygon points="165,50 240,50 235,55 160,55" fill="var(--brand-cyan)"/>
      <polygon points="240,47 281,47 281,52 238,52" fill="var(--brand-yellow)"/>
      <rect role="img" aria-label="Photo of a technician repairing a laser printer" x="0" y="55" width="281" height="210" fill="url(#repairPhoto)"/>
      <rect x="0" y="260" width="281" height="5" fill="var(--ink-black)"/>
      <polygon points="0,265 75,265 70,270 0,270" fill="var(--brand-yellow)"/>
      <polygon points="75,265 130,265 125,270 70,270" fill="var(--brand-cyan)"/>
      <polygon points="130,262 281,262 281,282 120,282" fill="var(--brand-magenta)"/>
    </svg>
    <p class="layer header-line back-header">GOT DIRTY PRINTER?</p>
    <div class="layer back-contact">
      <div class="brand-name"><span class="dot"></span>Kv Business Supplies</div>
      <p class="phone">555-203-4471</p>
      <p class="web">www.kvtoner.example</p>
    </div>
  </section>

</main>
</body>
</html>
```